Children's writer business card design

I write children's mystery and adventure books for 9-12 year olds. My logo is a small robin redbreast bird which I will appear on all my commercial stationery and websites. I have a 'silhouette' of a bird on the mock up on your site and I like this, although your designers might make it look even better. The bird is non-negotiable!

When I tried to do the back of the card I got a hallmark. I don't like this.

I would like the card to be modern, 'clean' and striking. Not too much colour. Definitely the red for the bird so it really stands out.

Target Market(s)

parents and grandparents of children 9-12 years old, booksellers, teachers

Industry/Entity Type

Business

Contact Information for Business Card

I have created a rough design using Cardloft which I hope you can access as this contains all of the information I want on my card.
The front has the following:
Mabel Frandsen
Writer & Education Consultant
www.mabelfrandsenauthor.example

04739158260
mfrandwrites@quillpost.example

The back has:
Books
The Copperfen Locket Puzzles (In bold)
The Riddle of the Copperfen Locket (in italics)
The Puzzle of the Copperfen (italics)
The Thorncastle Project (in bold)
Book 1: Stuck (italics)
Book 2: Unstuck (italics)

I'm happy for you to change the design provided the 'robin' stays.
Thank you.

Colors
ec2027

Requirements
Must have
• the robin redbreast bird logo - although it is fine to change how the bird looks.
Should not have
• no watermark

```html
<!DOCTYPE html>
<html lang="en">
<head>
<meta charset="utf-8">
<title>Mabel Frandsen – Business Card</title>
<link rel="stylesheet" href="https://fonts.googleapis.com/css2?family=Montserrat:wght@700&family=Open+Sans:ital,wght@0,300;0,400;1,300&display=swap">
<style>
  :root {
    --backdrop: #e9e6e1;
    --card: #111113;
    --ink: #f4f4f4;
    --ink-soft: #cfcfcf;
    --accent: #ec2027;
  }
  * { margin: 0; padding: 0; box-sizing: border-box; }
  html, body {
    width: 1200px; height: 899px; overflow: hidden;
    background: var(--backdrop);
  }
  .stage {
    position: relative; width: 1200px; height: 899px;
    display: flex; justify-content: center; align-items: center; gap: 90px;
  }
  .card {
    position: relative;
    width: 380px; height: 640px;
    background: var(--card);
    box-shadow: 0 10px 30px rgba(0,0,0,.25);
    color: var(--ink);
  }
  /* Front */
  .wordmark {
    position: absolute; top: 46px; right: 40px;
    font-family: "Montserrat", sans-serif; font-weight: 700;
    font-size: 28px; letter-spacing: -0.5px; color: var(--ink);
  }
  .contact {
    position: absolute; right: 40px; bottom: 50px;
    text-align: right;
    font-family: "Open Sans", sans-serif; font-weight: 300;
    font-size: 17px; line-height: 1.55; color: var(--ink-soft);
  }
  .contact .role { font-style: italic; }
  .rule {
    height: 3px; background: var(--accent); border: 0;
  }
  .contact .rule { width: 230px; margin: 10px 0 10px auto; }
  /* Back */
  .booklist {
    position: absolute; top: 40px; left: 34px; right: 30px;
    font-family: "Open Sans", sans-serif; font-size: 16px; line-height: 1.55;
  }
  .booklist .series,
  .booklist .title-bold {
    font-family: "Montserrat", sans-serif; font-weight: 700; font-size: 15.5px; color: var(--ink);
  }
  .booklist .title-italic { font-style: italic; font-weight: 300; color: var(--ink-soft); }
  .booklist .rule { width: 260px; margin-top: 8px; }
  .volumes {
    position: absolute; top: 300px; left: 34px;
    font-family: "Open Sans", sans-serif; font-style: italic; font-weight: 300;
    font-size: 19px; line-height: 1.6; color: var(--ink-soft);
  }
  .robin-mark {
    position: absolute; right: 40px; bottom: 40px;
    width: 22px; height: 28px;
    background: var(--accent);
    border-radius: 50% 50% 45% 45%;
  }
</style>
</head>
<body>
<main class="stage">
  <section class="card card-front">
    <div class="wordmark">Mabel Frandsen</div>
    <div class="contact">
      <p class="role">Mabel Frandsen Writer<br>&amp; Education Consultant</p>
      <hr class="rule">
      <p>04739158260</p>
      <p>mfrandwrites@quillpost.example</p>
      <p>www.mabelfrandsenauthor.example</p>
    </div>
  </section>

  <section class="card card-back">
    <div class="booklist">
      <p class="series">Books The Copperfen Locket Puzzles</p>
      <p class="title-italic">The Riddle of the Copperfen Locket</p>
      <p class="title-italic">The Puzzle of the Copperfen</p>
      <p class="title-bold">The Thorncastle Project</p>
      <hr class="rule">
    </div>
    <div class="volumes">
      <p>Book 1: Stuck</p>
      <p>Book 2: Unstuck</p>
    </div>
    <div class="robin-mark" role="img" aria-label="Red robin redbreast bird silhouette logo"></div>
  </section>
</main>
</body>
</html>
```